Poster design for Belgian waffles

We are a local frozen yogurt chain that will introduce a new product for winter. It is Belgian waffle. You can have it a plain, with toppings such fresh fruit or with our frozen yogurt. We need two posters, one for introduction of the product and one that has pricing on it.

Target Market(s)

College students and young professionals

Industry/Entity Type

Pricing

```html
<!DOCTYPE html>
<html lang="en">
<head>
<meta charset="utf-8">
<title>Belgian Waffle – Winter Poster</title>
<link rel="stylesheet" href="https://fonts.googleapis.com/css2?family=Lobster+Two:ital,wght@1,700&family=Roboto:wght@100;300;400;700&display=swap">
<style>
  :root {
    --sky-blue: #4a86c7;
    --sky-fade: #8fb4df;
    --brand-blue: #3d7ec4;
    --soft-blue: #8ab0dc;
    --price-blue: #9cbde4;
    --text-blue: #5d8fc9;
    --paper: #ffffff;
    --waffle-gold: #d9954a;
    --waffle-deep: #b86e2a;
    --plate: #eeeae4;
  }
  * { margin: 0; padding: 0; box-sizing: border-box; }
  html, body { width: 797px; height: 1200px; overflow: hidden; background: var(--paper); }
  .poster {
    position: relative;
    width: 797px;
    height: 1200px;
    overflow: hidden;
    font-family: "Roboto", "Helvetica Neue", Arial, sans-serif;
    background: linear-gradient(180deg, var(--sky-blue) 0px, var(--sky-blue) 230px, var(--sky-fade) 360px, var(--paper) 540px, var(--paper) 100%);
  }
  .headline {
    position: absolute;
    top: 98px;
    left: 0;
    width: 797px;
    text-align: center;
    font-family: "Lobster Two", "Brush Script MT", cursive;
    font-style: italic;
    font-weight: 700;
    font-size: 57px;
    line-height: 56px;
    color: var(--paper);
  }
  .rule {
    position: absolute;
    border: 0;
    border-top: 3px dotted currentColor;
  }
  .rule--header { top: 281px; left: 155px; width: 515px; color: var(--paper); }
  .rule--title { top: 757px; left: 213px; width: 395px; color: var(--brand-blue); }
  .rule--info { top: 1005px; left: 38px; width: 727px; color: var(--soft-blue); border-top-width: 2px; }

  .feature-photo {
    position: absolute;
    top: 332px;
    left: 156px;
    width: 513px;
    height: 345px;
    background: var(--paper);
    padding: 8px;
    box-shadow: 0 2px 8px rgba(0,0,0,0.25);
    overflow: hidden;
  }
  .feature-photo__image {
    width: 100%;
    height: 100%;
    background: radial-gradient(ellipse 62% 72% at 52% 50%, var(--waffle-gold) 0%, var(--waffle-deep) 62%, var(--plate) 64%, #d8d2ca 100%);
  }
  .intro-ribbon {
    position: absolute;
    top: 44px;
    left: -58px;
    width: 250px;
    height: 36px;
    background: var(--brand-blue);
    transform: rotate(-35deg);
    color: var(--paper);
    font-weight: 700;
    font-size: 20px;
    letter-spacing: 1px;
    text-align: center;
    line-height: 36px;
    border-top: 2px solid rgba(255,255,255,0.6);
    border-bottom: 2px solid rgba(255,255,255,0.6);
  }

  .product-title {
    position: absolute;
    top: 688px;
    left: 0;
    width: 797px;
    text-align: center;
    font-family: "Lobster Two", "Brush Script MT", cursive;
    font-style: italic;
    font-weight: 700;
    font-size: 54px;
    color: var(--brand-blue);
  }

  .menu-option {
    position: absolute;
    top: 800px;
    height: 175px;
  }
  .menu-option--plain { left: 30px; width: 226px; }
  .menu-option--fruit { left: 294px; width: 226px; }
  .menu-option--yogurt { left: 562px; width: 220px; }
  .menu-option__name {
    font-weight: 300;
    font-size: 38px;
    color: var(--brand-blue);
    text-align: center;
    line-height: 50px;
  }
  .menu-option__desc {
    margin-top: 16px;
    font-size: 7.6px;
    line-height: 12px;
    color: var(--text-blue);
  }
  .menu-option__desc b { font-weight: 700; color: var(--brand-blue); }
  .menu-option__price {
    margin-top: 14px;
    font-weight: 100;
    font-size: 37px;
    color: var(--price-blue);
    text-align: center;
  }
  .divider {
    position: absolute;
    top: 800px;
    height: 174px;
    border-left: 2px dotted var(--soft-blue);
  }
  .divider--one { left: 264px; }
  .divider--two { left: 536px; }

  .info {
    position: absolute;
    top: 1030px;
    left: 38px;
    width: 540px;
  }
  .info__heading {
    font-weight: 400;
    font-size: 18px;
    letter-spacing: 3.5px;
    color: var(--soft-blue);
  }
  .info__text {
    margin-top: 4px;
    font-size: 7.6px;
    line-height: 14.5px;
    letter-spacing: 0.4px;
    color: var(--price-blue);
  }
  .brand {
    position: absolute;
    top: 1068px;
    left: 604px;
    display: flex;
    align-items: center;
    gap: 7px;
    font-weight: 700;
    font-size: 26px;
    color: var(--brand-blue);
  }
  .brand__dot {
    width: 18px;
    height: 18px;
    border-radius: 50%;
    background: var(--brand-blue);
  }
  .footer-note {
    position: absolute;
    top: 1161px;
    left: 38px;
    width: 745px;
    font-weight: 700;
    font-size: 7.6px;
    letter-spacing: 0.4px;
    text-transform: uppercase;
    color: var(--soft-blue);
  }
</style>
</head>
<body>
<main class="poster">
  <h1 class="headline">Something to<br>look forward to<br>this Christmas Season.</h1>
  <hr class="rule rule--header">

  <figure class="feature-photo">
    <div class="feature-photo__image" role="img" aria-label="Golden Belgian waffle on a white plate"></div>
    <div class="intro-ribbon">INTRODUCING</div>
  </figure>

  <h2 class="product-title">Belgian Waffle</h2>
  <hr class="rule rule--title">

  <section class="menu-option menu-option--plain">
    <h3 class="menu-option__name">Plain</h3>
    <p class="menu-option__desc"><b>Description:</b> A warm golden waffle, crisp outside and soft inside, baked fresh to order and finished with a light dusting of sugar.</p>
    <p class="menu-option__price">$4.99</p>
  </section>
  <div class="divider divider--one"></div>
  <section class="menu-option menu-option--fruit">
    <h3 class="menu-option__name">*With Fruits</h3>
    <p class="menu-option__desc"><b>Description:</b> Our classic waffle topped with a generous mix of fresh strawberries, blueberries, banana and kiwi, cut daily in store.</p>
    <p class="menu-option__price">$5.99</p>
  </section>
  <div class="divider divider--two"></div>
  <section class="menu-option menu-option--yogurt">
    <h3 class="menu-option__name">*With Yogurt</h3>
    <p class="menu-option__desc"><b>Description:</b> Our classic waffle crowned with a swirl of your favorite frozen yogurt flavor and one topping of your choice from the bar.</p>
    <p class="menu-option__price">$7.99</p>
  </section>

  <hr class="rule rule--info">
  <section class="info">
    <h4 class="info__heading">ADDITIONAL INFORMATION</h4>
    <p class="info__text">Waffles are served from December 1 through the end of February at every participating store. Toppings are subject to seasonal availability and may vary by location. Prices do not include tax. Fruit and yogurt choices can be swapped at no extra charge. Ask our team about gluten and nut information before ordering. Students with a valid campus card receive ten percent off any waffle on weekdays after four. Warm up with a waffle between classes or after work.</p>
  </section>

  <div class="brand"><span>Frostmint</span><span class="brand__dot"></span></div>

  <p class="footer-note">Available for a limited time this winter at all Frostmint locations, while supplies last. Follow us for new flavors and seasonal specials.</p>
</main>
</body>
</html>
```